Book cover needed for Christian Non-Fiction Book

I need book cover design (eBook , Paperback, and possibly case laminate Hardcover) for use on PQL and Halvet Print.
Title: Go Forth Called
Sub-Title: Leaving Shelter and Walking in Faithful Purpose
Author: Owen Callery
Also on front cover "Forward by R. Lisel Marrow"

I like clean/simple designs. Below are links to examples of covers I like...
https://www.bookvantle.example/dp/X4821QPT7M?tag=plumwick-20&linkCode=ogi&th=1&psc=1
https://www.bookvantle.example/dp/X49KTRMWHZ?tag=plumwick-20&linkCode=ogi&th=1&psc=1
https://www.bookvantle.example/dp/X22HQC51NT?tag=plumwick-20&linkCode=ogi&th=1&psc=1
https://www.bookvantle.example/dp/X48F3WZPDR?tag=plumwick-20&linkCode=ogi&th=1&psc=1
https://www.bookvantle.example/dp/X4M7UVVCLE?tag=plumwick-20&linkCode=ogi&th=1&psc=1
https://www.bookvantle.example/dp/X2R9HNNKA6?tag=plumwick-20&linkCode=ogi&th=1&psc=1

The main idea for Go Forth Called is that God is a sending God and being "on the move" or journeying is central to God's character, and therefore God's people. I write about our hesitancy to "go," and how the Bible is full of stories about people "going" from Abraham to Jesus, to the disciples of Jesus.

The core biblical text is the Great Commission in Matthew 28:16-20, where Jesus sends out his followers, though some of them doubt.

This paragraph from the forward by R. Lisel Marrow captures the tone of the book well:
This book is a call amid the turmoil. Sacred scripture contains no shortage of narratives in which humans are pulled from their ordinary lives with an inciting incident whose stakes are high. These Biblical figures are lulled from complacency and comfort zones—and yet they are reluctant to serve because they question their ability and influence. Their lessons are relevant for us today: They, and we, are always called and sent with authority. The power of the Holy Spirit equips their “going”—and ours. It’s a sending out that looks less like mastery and more humility. It’s a sending out that is unequivocal service to others modelled in a rabbi-reformer who washed feet and touched the unclean.

I have previously published two shorter books and would be very interested in getting new covers for the old books these so that the three have a similar feel. Whichever designer I go with for "Go Forth Called" I would also want to work with on creating a "branded look" for the other two books.

Target Market(s)

Christian, Religion, Spirituality Readers

Requirements
Must have
• The front cover must have this copy...
Go Forth Called
Leaving Shelter and Walking in Faithful Purpose
Owen Callery
Forward by R. Lisel Marrow

Must be willing to do the full paperback and/or hardcover, but start with thefront cover please
Nice to have
• See attached files for some book covers I like

```html
<!DOCTYPE html>
<html lang="en">
<head>
<meta charset="utf-8">
<title>Go Forth Called — Front Cover</title>
<link href="https://fonts.googleapis.com/css2?family=Cinzel:wght@400;500;600&family=Cormorant+Garamond:ital,wght@1,400;1,500&display=swap" rel="stylesheet">
<style>
  :root {
    --backdrop: #d6d5d1;
    --cover-top: #3c3531;
    --cover-bottom: #4b4541;
    --gold: #d4b25a;
    --gold-deep: #8a6a22;
    --ivory: #f1eee8;
    --silver: #e6e6e6;
  }
  * { margin: 0; padding: 0; box-sizing: border-box; }
  html, body {
    width: 1200px;
    height: 864px;
    overflow: hidden;
    background: var(--backdrop);
  }
  .stage {
    width: 1200px;
    height: 864px;
    display: flex;
    align-items: center;
    justify-content: center;
  }
  .cover {
    position: relative;
    width: 540px;
    height: 810px;
    background: linear-gradient(160deg, var(--cover-top), var(--cover-bottom));
    color: var(--gold);
    text-align: center;
    box-shadow: 0 10px 30px rgba(0,0,0,0.25);
  }
  .title-word {
    position: absolute;
    left: 0;
    width: 100%;
    font-family: "Cinzel", serif;
    font-weight: 500;
    color: var(--gold);
    line-height: 1;
    letter-spacing: 0.02em;
  }
  .title-word--first { top: 62px; font-size: 80px; }
  .title-word--second { top: 182px; font-size: 80px; }
  .title-word--third { top: 556px; font-size: 80px; }
  .subtitle-line {
    position: absolute;
    left: 0;
    width: 100%;
    font-family: "Cormorant Garamond", serif;
    font-style: italic;
    font-weight: 500;
    font-size: 25px;
    color: var(--ivory);
  }
  .subtitle-line--first { top: 146px; }
  .subtitle-line--second { top: 268px; }
  .cover-art {
    position: absolute;
    left: 95px;
    top: 310px;
    width: 350px;
    height: 240px;
    border-radius: 50%;
    background: radial-gradient(ellipse at 48% 45%, var(--gold) 0%, #a88436 30%, rgba(90,80,70,0.6) 58%, rgba(75,69,65,0) 75%);
  }
  .foreword-credit {
    position: absolute;
    left: 0;
    width: 100%;
    top: 668px;
    font-family: "Cinzel", serif;
    font-size: 22px;
    color: var(--gold);
    letter-spacing: 0.03em;
  }
  .author-name {
    position: absolute;
    left: 0;
    width: 100%;
    top: 718px;
    font-family: "Cinzel", serif;
    font-weight: 500;
    font-size: 46px;
    color: var(--silver);
    letter-spacing: 0.02em;
  }
</style>
</head>
<body>
  <main class="stage">
    <section class="cover">
      <h1>
        <span class="title-word title-word--first">GO</span>
        <span class="title-word title-word--second">FORTH</span>
        <span class="title-word title-word--third">CALLED</span>
      </h1>
      <p class="subtitle-line subtitle-line--first">Leaving Shelter</p>
      <p class="subtitle-line subtitle-line--second">And Walking in Faithful Purpose</p>
      <div class="cover-art" role="img" aria-label="Golden fruit bound in tangled barbed wire, central cover illustration"></div>
      <p class="foreword-credit">FORWARD BY R. LISEL MARROW</p>
      <p class="author-name">OWEN CALLERY</p>
    </section>
  </main>
</body>
</html>
```